Business card/Stationary for mobile ultrasound company
Corvin Ultrasound Services, LLC
Business card/Stationary for mobile ultrasound company -
Creative Brief
Use specific fonts
can use a combination of fonts similar to logo
Professional
Tessa Quillon RDMS, RVT, RCS
Owner
P.O. Box 482 Brinmoor, NM 88099-0482
4quillons@mailnest.example
I am currently getting a website designed so i will add a web address and an updated email address specifically for the business. I am torn as to use a one sided or 2 sided card. So im open. I would rather not have the address on the card. Thanks
Innovative mobile technology focused on improving the QUALITY of patient care. (The wording can change but along this idea)

```html
<!DOCTYPE html>
<html lang="en">
<head>
<meta charset="utf-8">
<title>Corvin Ultrasound Services – Business Card</title>
<link href="https://fonts.googleapis.com/css2?family=Open+Sans:ital,wght@0,400;0,600;0,700;1,700&display=swap" rel="stylesheet">
<style>
  :root {
    --stage: #4d4d4d;
    --card-white: #ffffff;
    --panel-black: #0b0b0b;
    --band-grey: #a9a9a9;
    --ink: #1a1a1a;
    --ink-soft: #333333;
    --logo-white: #f2f2f2;
  }
  * { margin: 0; padding: 0; box-sizing: border-box; }
  html, body {
    width: 1200px;
    height: 780px;
    overflow: hidden;
    background: var(--stage);
    font-family: "Open Sans", Arial, sans-serif;
  }
  .business-card {
    position: absolute;
    left: 100px;
    top: 104px;
    width: 1000px;
    height: 572px;
    border-radius: 34px;
    overflow: hidden;
    background: var(--card-white);
    box-shadow: 0 10px 30px rgba(0,0,0,0.35);
  }
  .card-shapes {
    position: absolute;
    inset: 0;
    width: 1000px;
    height: 572px;
  }
  .card-shapes .black-panel { fill: var(--panel-black); }
  .card-shapes .grey-band { fill: var(--band-grey); }

  .company-name {
    position: absolute;
    left: 60px;
    top: 240px;
    width: 400px;
    text-align: center;
    color: var(--logo-white);
    font-weight: 600;
    line-height: 1.15;
  }
  .company-name .name-main {
    display: block;
    font-size: 66px;
    letter-spacing: 1px;
  }
  .company-name .name-sub {
    display: block;
    font-size: 20px;
    letter-spacing: 0.5px;
  }

  .holder {
    position: absolute;
    right: 70px;
    top: 36px;
    text-align: right;
    color: var(--ink);
  }
  .holder-name {
    font-size: 27px;
    font-weight: 700;
    font-style: italic;
  }
  .holder-name .credentials {
    font-size: 19px;
  }
  .holder-title {
    font-size: 21px;
    font-weight: 600;
    margin-top: 2px;
    margin-right: 6px;
  }

  .contact {
    position: absolute;
    right: 104px;
    text-align: right;
    color: var(--ink-soft);
    font-size: 20px;
    line-height: 1.4;
  }
  .contact-address { top: 262px; }
  .contact-phone { top: 364px; }
  .contact-email { top: 412px; }

  .contact-icon {
    position: absolute;
    right: 66px;
    width: 24px;
    height: 24px;
    fill: none;
    stroke: var(--ink);
    stroke-width: 2.4;
    stroke-linecap: round;
  }
  .icon-phone { top: 366px; }
  .icon-email { top: 416px; }
</style>
</head>
<body>
  <div class="business-card">
    <svg class="card-shapes" viewBox="0 0 1000 572" aria-hidden="true">
      <path class="grey-band" d="M470,0 L535,0 C540,200 450,420 250,572 L230,572 C420,420 500,200 470,0 Z"/>
      <path class="black-panel" d="M0,0 L470,0 C500,200 420,420 230,572 L0,572 Z"/>
    </svg>

    <div class="company-name">
      <span class="name-main">Corvin</span>
      <span class="name-sub">Ultrasound Services, LLC</span>
    </div>

    <div class="holder">
      <div class="holder-name">Tessa Quillon <span class="credentials">RDMS, RVT, RCS</span></div>
      <div class="holder-title">Owner</div>
    </div>

    <div class="contact contact-address">
      P.O. Box 482<br>
      Brinmoor, NM 88099-0482
    </div>
    <div class="contact contact-phone">575-555-0148</div>
    <div class="contact contact-email">4quillons@mailnest.example</div>

    <svg class="contact-icon icon-phone" viewBox="0 0 24 24" aria-hidden="true">
      <path d="M6 4 C4 6 4 10 8 15 C12 20 17 21 20 19"/>
      <path d="M6 4 L9 8"/>
      <path d="M20 19 L16 16"/>
    </svg>
    <svg class="contact-icon icon-email" viewBox="0 0 24 24" aria-hidden="true">
      <circle cx="12" cy="12" r="4"/>
      <path d="M16 8 V14 C16 17 21 17 21 12 A9 9 0 1 0 16 20"/>
    </svg>
  </div>
</body>
</html>
```